KVR Associates needs a web site

We need a web site for www.kvrassociates-example.com. KVR is a mergers and acquisition consulting company that focuses our buyer and seller services on logistics companies. We help put companies together, and help with legal and financial due diligence. We want the web site to express our service and show the logistics components. We want personalized images versus pictures of trucks and airplanes.

Our new logo uses Burgandy and grey colors. Image attached. We are not in to bold, big letters...classy, artistic, low key preferred. Confidentiality, experience, professional are what we want to express on the site.

All we expect for the first part of this project is a home page, and one subpage.  We are budgeting other funds for the technical aspects of the web site

Reason: All that I'm seeing so far is trucks, forklifts and planes. We are a legal mergers and acquisitions firm that focus on logistics. I like some of the images to say logistics, but really want it say legal, financial, and putting companies together. Will pay extra for the sub page if someone can impress us with a home page.

Reason: Swamped with another project at the moment...will work on this over the weekend and provide designer feedback and select final design by Tuesday

```html
<!DOCTYPE html>
<html lang="en">
<head>
<meta charset="utf-8">
<title>KVR Associates – Home</title>
<link href="https://fonts.googleapis.com/css2?family=Lato:wght@400;700&family=Cinzel:wght@400&family=Oswald:wght@300;400&display=swap" rel="stylesheet">
<style>
:root{
  --burgundy:#a3102f;
  --burgundy-dark:#7d0a22;
  --ink:#2b2b2b;
  --text:#3a3a3a;
  --grey:#8a8a8a;
  --line:#dedede;
  --footer:#1f1f1f;
  --page:#f7f7f7;
}
*{margin:0;padding:0;box-sizing:border-box}
html,body{width:962px;height:1200px;overflow:hidden}
body{position:relative;background:var(--page);font-family:"Lato",sans-serif;color:var(--text);font-size:11px}
.abs{position:absolute}

/* header */
.site-header{left:0;top:0;width:962px;height:90px;background:linear-gradient(#fafafa,#ececec);border-bottom:1px solid #d8d8d8}
.brand{left:108px;top:22px;display:flex;align-items:center;gap:10px}
.brand-mark{width:16px;height:16px;background:var(--burgundy)}
.brand-name{font-size:30px;font-weight:400;color:var(--burgundy);letter-spacing:1px}
.brand-tag{font-size:13px;color:#555;letter-spacing:1px;line-height:1.1;border-left:1px solid #555;padding-left:10px}
.phone{left:760px;top:15px;font-size:12.5px;color:#444;display:flex;align-items:center;gap:4px}
.main-nav{left:392px;top:63px;display:flex;font-size:12px;color:#333}
.main-nav a{color:inherit;text-decoration:none;padding:2px 12px;border-left:1px solid #ddd;line-height:14px}
.main-nav a:first-child{border-left:none}
.main-nav a.active{background:var(--burgundy);color:#fff;font-weight:700;border-radius:2px;padding:2px 7px;margin-right:6px}

/* hero */
.hero{left:0;top:91px;width:962px;height:359px;background:linear-gradient(90deg,#7aa3c9 0%,#c9d4dc 14%,#7d6e66 40%,#8a7364 70%,#a88d78 88%,#c9c0b8 100%)}
.hero-frame{left:105px;top:112px;width:752px;height:293px;background:#fff;box-shadow:0 2px 6px rgba(0,0,0,.3)}
.hero-photo{left:109px;top:116px;width:744px;height:285px;background:linear-gradient(90deg,#d9dde0 0%,#c7b7a6 30%,#e1e4e6 55%,#2d3848 75%,#bfc6cc 100%)}
.hero-caption{left:109px;top:368px;width:744px;height:33px;background:rgba(25,25,25,.82);color:#fff;font-family:"Cinzel",serif;font-size:16px;letter-spacing:.6px;text-align:center;line-height:33px}
.slider-tab{left:430px;top:405px;width:100px;height:27px}

/* services */
.service{width:180px;text-align:center}
.service-icon{width:86px;height:86px;border-radius:50%;border:1px solid #d3d3d3;background:#fff;margin:0 auto;display:flex;align-items:center;justify-content:center}
.service-icon.on{background:var(--burgundy);border-color:var(--burgundy)}
.service h3{font-size:15px;font-weight:400;color:#2a2a2a;margin-top:14px}
.service p{font-size:11px;line-height:14.5px;color:#444;margin-top:6px}
.btn{display:inline-block;background:var(--burgundy);color:#fff;font-size:11px;font-weight:700;padding:3px 7px;border-radius:1px;line-height:12px}
.service .btn{margin-top:11px}
.email-field{width:166px;height:22px;border:1px solid #ccc;background:#fff;margin:7px auto 0;font-size:10px;color:#999;text-align:left;padding:4px 7px}
.divider{left:110px;top:693px;width:742px;height:1px;background:linear-gradient(90deg,transparent,#ddd 20%,#ddd 80%,transparent)}

/* panels */
.panel{top:720px;width:236px;height:228px}
.panel-body{position:absolute;left:4px;right:4px;top:4px;bottom:0;background:#fff;border:1px solid #e2e2e2;box-shadow:0 6px 6px -4px rgba(0,0,0,.25)}
.panel-head{position:absolute;left:-2px;right:-2px;top:10px;height:30px;background:linear-gradient(#3a3a3a,#151515);color:#fff;font-family:"Cinzel",serif;font-weight:400;font-size:14.5px;text-transform:uppercase;letter-spacing:.6px;line-height:30px;padding-left:10px;white-space:nowrap}
.panel-badge{position:absolute;right:8px;top:2px;width:26px;height:26px;border-radius:50%;background:#fff;display:flex;align-items:center;justify-content:center}
.panel-badge i{display:block;width:20px;height:20px;border-radius:50%;background:var(--burgundy)}
.panel-inner{position:absolute;left:12px;right:12px;top:52px}
.team-photo{width:208px;height:86px;background:linear-gradient(90deg,#5e6d7e,#c9b6a4 45%,#3d4a5c 70%,#d5d1cc)}
.panel p{font-size:10px;line-height:16px;color:#333}
.more{position:absolute;right:12px;bottom:9px;color:var(--burgundy);font-size:10.5px;font-weight:700}
.news-item{display:flex;gap:5px;padding-bottom:4px;margin-bottom:4px;border-bottom:1px dotted #ccc}
.news-item:last-child{border-bottom:none;margin-bottom:0}
.date{width:29px;flex:none;text-align:center;font-weight:700;color:#fff;margin-top:2px}
.date b{display:block;background:var(--burgundy);font-size:11px;line-height:15px}
.date span{display:block;background:#666;font-size:8.5px;line-height:11px}
.news-item p{font-size:10px;line-height:14px;white-space:nowrap}
.news-item strong{color:#222}
.avatar{width:66px;height:66px;border-radius:50%;border:3px solid #eee;background:radial-gradient(circle at 50% 40%,#c7a08a,#4a5668 70%);float:left;margin-right:9px}
.testimonial p{line-height:15.5px}

/* footer */
.footer-wave{left:0;top:916px;width:962px;height:284px}
.footer-links{top:1115px;font-size:11px;color:#fff;line-height:22px;list-style:none}
.footer-links li::before{content:"•";color:#999;font-size:8px;margin-right:6px;vertical-align:1px}
.map{left:384px;top:1084px;width:190px;height:70px;border:2px solid #bbb;background:linear-gradient(135deg,#e8e1c7,#f0c47a 40%,#e6dfd0 60%,#a9c8e0)}
.address{left:382px;top:1162px;color:#fff;font-size:10.5px;line-height:13px;display:flex;gap:6px}
.consult{left:623px;top:1061px;font-family:"Oswald",sans-serif;font-weight:300;color:#fff;font-size:14.5px;line-height:23px}
.appt{display:inline-block;background:linear-gradient(#fff,#ddd);color:#222;font-size:12px;padding:0 7px;line-height:18px;margin-left:4px;border:1px solid #999;vertical-align:1px;font-weight:400}
.social{left:682px;top:1131px;display:flex;gap:10px}
.social i{display:block;width:16px;height:16px;border-radius:50%;background:#cfcfcf}
.copyright{left:650px;top:1176px;width:186px;text-align:right;font-size:9px;color:#ddd}
</style>
</head>
<body>

<header class="site-header abs">
  <div class="brand abs">
    <span class="brand-mark"></span>
    <span class="brand-name">KVR</span>
    <span class="brand-tag">KVR<br>ASSOCIATES</span>
  </div>
  <div class="phone abs">
    <svg width="12" height="12" viewBox="0 0 24 24"><path fill="#a3102f" d="M6.6 10.8a15 15 0 0 0 6.6 6.6l2.2-2.2c.3-.3.7-.4 1-.2 1.1.4 2.3.6 3.6.6.6 0 1 .4 1 1V20c0 .6-.4 1-1 1A17 17 0 0 1 3 4c0-.6.4-1 1-1h3.5c.6 0 1 .4 1 1 0 1.3.2 2.5.6 3.6.1.3 0 .7-.2 1z"/></svg>
    555 014 2290
  </div>
  <nav class="main-nav abs">
    <a class="active">Home</a><a>About</a><a>Consulting Services</a><a>News &amp; Events</a><a>FAQ's</a><a>Contact</a>
  </nav>
</header>

<section class="hero abs" role="img" aria-label="Background photo of a logistics yard with a truck and a worker"></section>
<div class="hero-frame abs"></div>
<div class="hero-photo abs" role="img" aria-label="Photo of three business people in a friendly meeting"></div>
<div class="hero-caption abs">We are a legal mergers and acquisitions firm that focus on logistics.</div>
<svg class="slider-tab abs" viewBox="0 0 100 27">
  <path d="M0 0 H100 L88 22 Q86 27 80 27 H20 Q14 27 12 22 Z" fill="#ececec"/>
  <circle cx="24" cy="11" r="4.5" fill="#c4101c"/>
  <circle cx="41" cy="11" r="4.5" fill="#555"/>
  <circle cx="58" cy="11" r="4.5" fill="#555"/>
  <circle cx="75" cy="11" r="4.5" fill="#555"/>
</svg>

<section>
  <div class="service abs" style="left:106px;top:481px">
    <div class="service-icon on">
      <svg width="44" height="44" viewBox="0 0 44 44"><rect x="4" y="6" width="28" height="28" rx="2" fill="#fff"/><rect x="4" y="6" width="28" height="6" fill="#ddd"/><g fill="#a3102f"><rect x="8" y="16" width="4" height="4"/><rect x="15" y="16" width="4" height="4"/><rect x="8" y="23" width="4" height="4"/><rect x="15" y="23" width="4" height="4"/></g><circle cx="32" cy="30" r="9" fill="#fff" stroke="#a3102f" stroke-width="2"/><path d="M32 25v5h4" stroke="#a3102f" stroke-width="2" fill="none"/></svg>
    </div>
    <h3>Business Planning</h3>
    <p>Lorem ipsum dolor sit amet,<br>consect ectetuer adipiscing elit,<br>sed diamgra nonummy.</p>
    <span class="btn">Read More</span>
  </div>
  <div class="service abs" style="left:287px;top:481px">
    <div class="service-icon">
      <svg width="44" height="44" viewBox="0 0 44 44"><rect x="4" y="20" width="24" height="16" fill="#222"/><rect x="7" y="23" width="18" height="10" fill="#fff"/><g fill="#222"><rect x="9" y="28" width="2" height="4"/><rect x="13" y="26" width="2" height="6"/><rect x="17" y="25" width="2" height="7"/><rect x="21" y="27" width="2" height="5"/></g><circle cx="29" cy="12" r="5" fill="#222"/><path d="M20 36 Q22 20 29 20 Q38 20 38 36Z" fill="#222"/></svg>
    </div>
    <h3>Business Merger</h3>
    <p>Lorem ipsum dolor sit amet,<br>consect ectetuer adipiscing elit,<br>sed diamgra nonummy.</p>
    <span class="btn">Read More</span>
  </div>
  <div class="service abs" style="left:466px;top:481px;width:210px">
    <div class="service-icon">
      <svg width="44" height="44" viewBox="0 0 44 44"><rect x="8" y="4" width="28" height="20" fill="none" stroke="#222" stroke-width="2"/><g fill="#222"><rect x="24" y="14" width="2" height="6"/><rect x="28" y="11" width="2" height="9"/><circle cx="9" cy="34" r="3"/><circle cx="22" cy="34" r="3"/><circle cx="35" cy="34" r="3"/><rect x="5" y="38" width="8" height="4"/><rect x="18" y="38" width="8" height="4"/><rect x="31" y="38" width="8" height="4"/><rect x="15" y="12" width="4" height="14"/></g></svg>
    </div>
    <h3>Acquisition (M&amp;A) Advisory</h3>
    <p>Lorem ipsum dolor sit amet,<br>consect ectetuer adipiscing elit,<br>sed diamgra nonummy.</p>
    <span class="btn">Read More</span>
  </div>
  <div class="service abs" style="left:675px;top:481px">
    <div class="service-icon">
      <svg width="44" height="32" viewBox="0 0 44 32"><rect x="2" y="2" width="40" height="28" fill="#222"/><path d="M4 4 L22 18 L40 4" stroke="#fff" stroke-width="2.5" fill="none"/><path d="M4 28 L17 15 M40 28 L27 15" stroke="#fff" stroke-width="2" fill="none"/></svg>
    </div>
    <h3>Newsletter Signup</h3>
    <div class="email-field">Enter your email here</div>
    <p style="margin-top:9px">Signup for KVR Newsletter!</p>
    <span class="btn" style="margin-top:9px">Subscribe</span>
  </div>
</section>

<div class="divider abs"></div>

<section>
  <article class="panel abs" style="left:106px">
    <div class="panel-body">
      <div class="panel-inner" style="top:50px;left:10px;right:10px">
        <div class="team-photo" role="img" aria-label="Photo of a team of professionals in a meeting"></div>
        <p style="margin-top:6px">KVR can help you formulate and execute your<br>growth strategy. We take a strategic and<br>consultative approach...</p>
      </div>
      <span class="more">Read More</span>
    </div>
    <h2 class="panel-head">What We Do<span class="panel-badge"><i></i></span></h2>
  </article>

  <article class="panel abs" style="left:363px">
    <div class="panel-body">
      <div class="panel-inner" style="left:10px;right:6px">
        <div class="news-item"><div class="date"><b>22</b><span>JULY</span></div><p><strong>Duis aute irure dolor in repre</strong><br>Duis autem vel eum iriure dolor inbo<br>dolor hendrerit in amet vulputate.</p></div>
        <div class="news-item"><div class="date"><b>22</b><span>JULY</span></div><p><strong>Duis aute irure dolor in repre</strong><br>Duis autem vel eum iriure dolor inbo<br>dolor hendrerit in amet vulputate.</p></div>
        <div class="news-item"><div class="date"><b>22</b><span>JULY</span></div><p><strong>Duis aute irure dolor in repre</strong><br>Duis autem vel eum iriure dolor inbo<br>dolor hendrerit in amet vulputate.</p></div>
      </div>
      <span class="more">Read More</span>
    </div>
    <h2 class="panel-head">News &amp; Events<span class="panel-badge"><i></i></span></h2>
  </article>

  <article class="panel abs" style="left:618px">
    <div class="panel-body">
      <div class="panel-inner testimonial" style="top:52px;left:8px;right:8px">
        <div class="avatar" role="img" aria-label="Portrait photo of a client"></div>
        <p><strong style="color:#222"><span style="color:#bbb;font-size:15px">“</span> Lorem ipsum dolor sita</strong><br>Sed diam nonummy euismli<br>tincidunt laorlpi dolore smit<br>aliquam erat volutpat.</p>
        <p style="clear:both;padding-top:8px">Duis autem vel eum iriure dolor in dolor hend<br>sit in amet sit vulputate velit uisam.</p>
        <p style="margin-top:4px;font-weight:700;color:#222">- Mr. Client Name</p>
      </div>
      <span class="more">Read More</span>
    </div>
    <h2 class="panel-head">Client Testimonials<span class="panel-badge"><i></i></span></h2>
  </article>
</section>

<footer>
  <svg class="footer-wave abs" viewBox="0 0 962 284" preserveAspectRatio="none">
    <path d="M0 14 Q120 120 380 132 Q700 140 962 56 V284 H0Z" fill="var(--footer)"/>
    <path d="M0 0 Q90 100 330 118 Q640 134 962 58 L962 66 Q650 150 340 142 Q90 132 0 40Z" fill="#cfcfcf"/>
    <path d="M0 0 Q90 92 330 110 Q600 120 920 58 Q600 104 360 104 Q110 96 0 0Z" fill="var(--burgundy)"/>
    <path d="M0 60 Q100 132 340 142 Q650 150 962 66 V284 H0Z" fill="var(--footer)"/>
  </svg>

  <ul class="footer-links abs" style="left:114px"><li>Home</li><li>About</li><li>Consulting Services</li></ul>
  <ul class="footer-links abs" style="left:234px"><li>News &amp; Events</li><li>FAQ's</li><li>Contact</li></ul>

  <div class="map abs" role="img" aria-label="Street map of the office location"></div>
  <div class="address abs">
    <svg width="14" height="20" viewBox="0 0 14 20"><path d="M7 0a7 7 0 0 0-7 7c0 5 7 13 7 13s7-8 7-13a7 7 0 0 0-7-7z" fill="#fff"/><circle cx="7" cy="7" r="2.5" fill="#1f1f1f"/></svg>
    <span>KVR Associates<br>Harbor City, Bayport, Lakeview.</span>
  </div>

  <div class="consult abs">Schedule Free Consultation <span class="appt">Appointment</span><br>Or Call Us on : (555) 014 2290</div>
  <div class="social abs"><i></i><i></i><i></i><i></i></div>
  <div class="copyright abs">© Copyright 2013 KVR Associates.</div>
</footer>

</body>
</html>
```